Tidewater Family Insurance (TFI

Project Brief for TFI Insurance Website Redesign

Background:
TFI is a leading insurance company based in the Caribbean, offering a wide range of insurance products and services. We aim to redesign our website to reflect a modern, user-friendly, and vibrant online presence that resonates with our diverse Caribbean clientele, particularly reflecting the African American and Caribbean demographic.

Objective:
To create a modern, engaging, and informative website that effectively communicates TFI's insurance products and services to current and potential clients, with a focus on lifestyle-oriented imagery and content.

Target Audience:
Our primary audience includes individuals, families, and businesses in the Caribbean, especially those looking for reliable and comprehensive insurance solutions. The design should appeal to a diverse range of ages but should be particularly attractive to middle-aged professionals.

Design Requirements:

Modern, clean, and user-friendly interface.
Vibrant and lifestyle-oriented imagery and graphics, featuring people of African American or Caribbean ethnicity to reflect our client base.
Mobile-responsive design to ensure accessibility on all devices.
Intuitive navigation and layout to enhance user experience.
Website Pages:
The website should include the following pages:

Home
Whole Life Insurance
Health Insurance
Motor Insurance
Group Insurance
Health Claim
About Us
Agents
Forms
Get a Quote
Investor Relations
Insurance Education
Set an Appointment
Contact Us
Additional Pages/Suggestions:

Testimonials: showcasing customer reviews and stories.
FAQs: addressing common questions about insurance policies and processes.
Careers: highlighting employment opportunities and promoting TFI as a great place to work.
News and Updates: featuring the latest news, updates, and tips related to insurance and lifestyle.
Accessibility Features: ensuring the site is accessible to users with disabilities.
Design Options:
We would like to receive at least two design options to choose from, each presenting a different look and feel while adhering to the design requirements outlined above.

Imagery and Content:

Use high-quality, authentic images that represent the diverse lifestyles of our Caribbean audience.
Ensure that content is clear, concise, and easy to understand, avoiding insurance jargon where possible.
Highlight key products and services clearly on the homepage to direct users effectively.
Functionality Requirements:

SEO optimized to enhance visibility on search engines.
Fast loading times to improve user experience and reduce bounce rates.
Secure online forms for quotes, appointments, and claims submissions.
Integration with social media platforms to enhance engagement and reach.
Submission Guidelines:

Proposals should include detailed design mockups for key pages.
Outline the proposed user journey and experience.
Provide an estimated timeline and budget for the project.
Include case studies or examples of previous work, particularly in the insurance or financial services sectors.
Evaluation Criteria:

Creativity and originality of the design.
Alignment with TFI’s brand and target audience.
User experience and site navigation.
Technical feasibility and scalability.
Cost-effectiveness and adherence to budget and timeline.
Deadline for Submission:
March 4, 2024

ALSO I have attached some brand assets to assist.

Companies, Car Owners, Home Builders, Groups wanting Health Insurance, Private and Business

Insurance

5+ page

Sans Serif

00AB8E
00BBA5
67D7C9
C6EFE9
E9F9F6
FFF300
FFF600
FEFA6F
FFFEC7
FFFEE8
EB3D1F
EC4F4E
F09395
F8D3D4
FCEDEE

• Provided Logo, African American people
• They should ask
• No other ethnicity but African American

```html
<!DOCTYPE html>
<html lang="en">
<head>
<meta charset="utf-8">
<title>Tidewater Family Insurance</title>
<link href="https://fonts.googleapis.com/css2?family=Poppins:ital,wght@0,400;0,500;0,600;0,700;0,800;1,400;1,800&display=swap" rel="stylesheet">
<style>
:root{
  --green:#3dae49;
  --green-light:#6cc477;
  --green-pale:#e6f4e8;
  --ink:#1e1e1e;
  --dark:#231f20;
  --grey-text:#7a7a7a;
  --light-bg:#f3f3f3;
  --line:#d6d6d6;
  --white:#ffffff;
}
*{margin:0;padding:0;box-sizing:border-box}
html,body{width:1200px;height:4622px;overflow:hidden}
body{font-family:'Poppins',sans-serif;color:var(--ink);background:var(--white);position:relative}
a{color:inherit;text-decoration:none}

/* header */
.header{position:absolute;top:0;left:0;width:1200px;height:115px;background:var(--white)}
.brand{position:absolute;left:110px;top:18px;display:flex;align-items:center;gap:10px}
.brand-dot{width:44px;height:44px;border-radius:50%;background:var(--green)}
.brand-name{font-size:21px;font-weight:700;color:var(--green);line-height:1.1;width:250px}
.btn{display:inline-flex;align-items:center;justify-content:center;background:var(--green);color:var(--white);font-weight:600;border-radius:40px}
.btn-appt{position:absolute;left:757px;top:10px;width:228px;height:50px;font-size:15px}
.btn-login{position:absolute;left:990px;top:10px;width:98px;height:50px;font-size:15px;background:var(--white);color:var(--green);border:2px solid var(--green)}
.utility{position:absolute;right:112px;top:76px;display:flex;gap:17px;font-size:14.5px;color:#444}
.mainnav{position:absolute;top:115px;left:0;width:1200px;height:50px;background:var(--dark);display:flex;justify-content:center;align-items:center;gap:36px;color:var(--white);font-size:16px;font-weight:500}

/* hero */
.hero{position:absolute;top:165px;left:0;width:1200px;height:573px;
  background:
    linear-gradient(90deg,rgba(20,40,40,.45) 0%,rgba(20,40,40,.15) 35%,rgba(0,0,0,0) 55%),
    radial-gradient(ellipse 180px 230px at 620px 190px,#e2a72a 0%,rgba(226,167,42,0) 100%),
    radial-gradient(ellipse 140px 150px at 820px 250px,#c43a3a 0%,rgba(196,58,58,0) 100%),
    radial-gradient(ellipse 220px 200px at 680px 370px,#7d2a32 0%,rgba(125,42,50,0) 100%),
    radial-gradient(ellipse 200px 160px at 900px 370px,#556048 0%,rgba(85,96,72,0) 100%),
    radial-gradient(ellipse 320px 120px at 620px 480px,#8a96a6 0%,rgba(138,150,166,0) 100%),
    linear-gradient(180deg,rgba(0,0,0,0) 62%,#9aa3aa 80%,#6f757a 100%),
    radial-gradient(ellipse 420px 260px at 80px 120px,#6f7f4a 0%,rgba(111,127,74,0) 100%),
    linear-gradient(180deg,#d9e2e8 0%,#b9cbd6 40%,#9fb6c4 62%,#7f8f98 100%)}
.hero-kicker{position:absolute;left:111px;top:210px;font-size:31px;font-weight:600;color:var(--white)}
.hero-title{position:absolute;left:110px;top:252px;font-size:58px;font-weight:800;font-style:italic;color:var(--white);letter-spacing:1px}
.btn-quote{position:absolute;left:111px;top:355px;width:214px;height:68px;font-size:19px}

/* welcome */
.welcome{position:absolute;top:738px;left:0;width:1200px;height:532px}
.welcome-mark{position:absolute;left:110px;top:40px;width:385px;height:440px;display:flex;flex-direction:column;align-items:center;justify-content:center;gap:24px}
.welcome-mark .circle{width:250px;height:250px;border-radius:50%;background:var(--green)}
.welcome-mark .name{font-size:28px;font-weight:700;color:var(--green);text-align:center;line-height:1.3}
.kicker{font-size:30px;font-weight:500;color:var(--ink);line-height:1.2}
.heading{font-size:40px;font-weight:700;color:var(--green);line-height:1.2}
.body-copy{font-size:16px;line-height:28.5px;color:#444}
.welcome-text{position:absolute;left:592px;top:76px;width:500px}
.welcome-text .body-copy{margin-top:22px}
.play{position:absolute;left:592px;top:406px}

/* services */
.services{position:absolute;top:1270px;left:0;width:1200px;height:813px;background:var(--light-bg)}
.center-head{text-align:center}
.services .center-head{position:absolute;top:58px;width:1200px}
.svc{position:absolute;width:327px;text-align:center}
.svc svg{display:block;margin:0 auto}
.svc h3{font-size:21px;font-weight:500;margin-top:18px}
.svc p{font-size:16px;line-height:27px;color:var(--grey-text);margin-top:12px;padding:0 4px}
.vline{position:absolute;width:1px;background:var(--line)}
.hline{position:absolute;height:1px;background:var(--line)}

/* feature rows */
.feature{position:absolute;width:430px}
.feature .body-copy{margin-top:22px}
.btn-more{width:165px;height:62px;font-size:17px;margin-top:36px}
.photo{position:absolute}
.photo-meeting{left:604px;top:2166px;width:484px;height:388px;
  background:
    radial-gradient(ellipse 70px 80px at 100px 120px,#4a3428 0%,rgba(74,52,40,0) 100%),
    radial-gradient(ellipse 110px 150px at 110px 260px,#5a7ea6 0%,rgba(90,126,166,0) 100%),
    radial-gradient(ellipse 90px 130px at 250px 280px,#7fa6cf 0%,rgba(127,166,207,0) 100%),
    radial-gradient(ellipse 120px 200px at 420px 200px,#c9ced6 0%,rgba(201,206,214,0) 100%),
    radial-gradient(ellipse 70px 80px at 380px 80px,#3a2a22 0%,rgba(58,42,34,0) 100%),
    linear-gradient(180deg,rgba(0,0,0,0) 82%,#b67a4a 90%,#8a5836 100%),
    linear-gradient(135deg,#eef0f2 0%,#dde2e7 50%,#f4f2ee 100%)}
.photo-laptop{left:110px;top:2634px;width:484px;height:388px;
  background:
    radial-gradient(ellipse 130px 110px at 330px 190px,#e9eef6 0%,rgba(233,238,246,0) 100%),
    radial-gradient(ellipse 150px 120px at 300px 330px,#6a6560 0%,rgba(106,101,96,0) 100%),
    radial-gradient(ellipse 130px 200px at 110px 230px,#2e2a28 0%,rgba(46,42,40,0) 100%),
    linear-gradient(90deg,#4a4440 0%,#8e8377 45%,#cfc7bc 80%,#e6e1da 100%)}

/* testimonials */
.testimonials{position:absolute;top:3105px;left:0;width:1200px;height:470px;
  background:
    radial-gradient(ellipse 260px 200px at 880px 200px,rgba(40,120,50,.55) 0%,rgba(40,120,50,0) 100%),
    radial-gradient(ellipse 200px 220px at 420px 300px,rgba(40,120,50,.45) 0%,rgba(40,120,50,0) 100%),
    radial-gradient(ellipse 240px 160px at 150px 80px,rgba(90,185,100,.6) 0%,rgba(90,185,100,0) 100%),
    linear-gradient(90deg,#48ad53,#52b55d 50%,#45a950)}
.testimonials .center-head{position:absolute;top:50px;width:1200px}
.testimonials .kicker{color:var(--white)}
.testimonials .heading{color:var(--white);font-size:38px}
.quote{position:absolute;left:180px;top:186px;width:840px;text-align:center;font-style:italic;font-size:20px;line-height:31.5px;color:var(--white)}
.quote-name{position:absolute;top:340px;width:1200px;text-align:center;font-size:18px;font-weight:600;color:var(--white)}
.dots{position:absolute;top:398px;left:546px;display:flex;gap:6px}
.dots span{width:24px;height:3px;background:rgba(255,255,255,.5)}
.dots span:first-child{background:var(--white)}

/* appointment */
.appointment{position:absolute;top:3575px;left:0;width:1200px;height:585px;background:var(--white)}
.appointment .watermark{position:absolute;left:440px;top:80px;width:320px;height:440px;border-radius:50%;background:#f6f6f6}
.appointment .center-head{position:absolute;top:86px;width:1200px}
.field{position:absolute;background:var(--white);box-shadow:0 2px 8px rgba(0,0,0,.12);font-size:16px;color:#555;padding:14px 18px}
.btn-submit{position:absolute;left:543px;top:428px;width:114px;height:60px;font-size:17px}

/* footer */
.footer{position:absolute;top:4160px;left:0;width:1200px;height:462px;background:var(--dark);color:var(--white)}
.footer-brand{position:absolute;left:110px;top:50px;width:190px;text-align:center}
.footer-brand .circle{width:120px;height:120px;margin:0 auto;border:6px solid var(--white);border-radius:50%}
.footer-brand .abbr{font-size:62px;font-weight:700;line-height:1;margin-top:18px}
.footer-brand .name{font-size:15px;font-weight:600;margin-top:10px;letter-spacing:1px;line-height:1.3}
.footer h4{font-size:21px;font-weight:600}
.links{position:absolute;top:72px;font-size:16px;line-height:28.5px}
.contact{position:absolute;left:820px;top:72px;width:280px;font-size:16px;line-height:26px}
.contact li{list-style:none;display:flex;gap:10px;margin-bottom:26px}
.contact svg{flex:none;margin-top:5px}
.footer-rule{position:absolute;left:110px;top:366px;width:978px;height:1px;background:#4a4546}
.copyright{position:absolute;left:110px;top:396px;font-size:16px}
.social{position:absolute;left:941px;top:386px;display:flex;gap:8px}
.social span{width:44px;height:44px;border-radius:50%;border:2px solid var(--green);display:flex;align-items:center;justify-content:center}
.social span i{width:12px;height:12px;border-radius:50%;background:var(--green)}
</style>
</head>
<body>

<header class="header">
  <div class="brand"><span class="brand-dot"></span><span class="brand-name">Tidewater Family Insurance</span></div>
  <a class="btn btn-appt" href="#">SET AN APPOINTMENT</a>
  <a class="btn btn-login" href="#">LOGIN</a>
  <nav class="utility"><a href="#">Testimonials</a><a href="#">FAQs</a><a href="#">Careers</a><a href="#">News and Updates</a><a href="#">Accessibility Features</a></nav>
</header>
<nav class="mainnav"><a href="#">Services</a><a href="#">About Us</a><a href="#">Agents</a><a href="#">Forms</a><a href="#">Investor Relations</a><a href="#">Insurance Education</a><a href="#">Contact Us</a></nav>

<section class="hero" role="img" aria-label="Family of four laughing together on a wooden lakeside dock">
  <p class="hero-kicker">ALWAYS HERE FOR YOU...</p>
  <p class="hero-title">ALWAYS</p>
  <a class="btn btn-quote" href="#">GET A QUOTE</a>
</section>

<section class="welcome">
  <div class="welcome-mark"><span class="circle"></span><span class="name">Tidewater Family<br>Insurance</span></div>
  <div class="welcome-text">
    <p class="kicker">WELCOME TO</p>
    <h1 class="heading">TIDEWATER FAMILY<br>INSURANCE</h1>
    <p class="body-copy">Lorem Ipsum is simply dummy text of the printing and types etting industry. Lorem Ipsum has been the industry's standa rd dummy text ever since the 1500s, when an unknown printer took a galley of type and scrambled e dolor in reprehenderit in voluptate velit esse cillum dolore.</p>
  </div>
  <svg class="play" width="64" height="64" viewBox="0 0 64 64" aria-label="Play video"><circle cx="32" cy="32" r="30" fill="var(--green)"/><circle cx="32" cy="32" r="25" fill="#1e1e1e"/><path d="M26 21 L44 32 L26 43 Z" fill="#fff"/></svg>
</section>

<section class="services">
  <div class="center-head"><p class="kicker">OUR</p><h2 class="heading">SERVICES</h2></div>
  <div class="vline" style="left:437px;top:188px;height:552px"></div>
  <div class="vline" style="left:763px;top:188px;height:552px"></div>
  <div class="hline" style="left:113px;top:463px;width:975px"></div>

  <div class="svc" style="left:110px;top:195px">
    <svg width="90" height="90" viewBox="0 0 90 90" fill="none" stroke="#1e1e1e" stroke-width="2.5"><rect x="12" y="10" width="48" height="66" rx="3"/><rect x="26" y="5" width="20" height="10" rx="2"/><path d="M20 30h28M20 42h28M20 54h22M20 66h16"/><path d="M62 40l14 5v12c0 9-6 15-14 18-8-3-14-9-14-18V45z" stroke="var(--green)"/><path d="M62 50v14M55 57h14" stroke="var(--green)"/></svg>
    <h3>Health Insurance</h3>
    <p>Duis aute irure dolor in reprehenderit in voluptate velit esse cillum dolore eu fugiat nulla pariatur</p>
  </div>
  <div class="svc" style="left:437px;top:195px">
    <svg width="90" height="90" viewBox="0 0 90 90" fill="none" stroke="#1e1e1e" stroke-width="2.5"><rect x="10" y="8" width="44" height="64" rx="3"/><path d="M18 22h28M18 32h28M18 42h18M18 52h14"/><path d="M58 14l12 4v10c0 7-5 12-12 14-7-2-12-7-12-14V18z" stroke="var(--green)"/><path d="M53 27l4 4 8-8" stroke="var(--green)"/><path d="M40 70l6-10h24l6 10v8H40z" stroke="var(--green)"/><circle cx="48" cy="78" r="4" stroke="var(--green)"/><circle cx="68" cy="78" r="4" stroke="var(--green)"/></svg>
    <h3>Motor Insurance</h3>
    <p>Duis aute irure dolor in reprehenderit in voluptate velit esse cillum dolore eu fugiat nulla pariatur</p>
  </div>
  <div class="svc" style="left:763px;top:195px">
    <svg width="90" height="90" viewBox="0 0 90 90" fill="none" stroke="#1e1e1e" stroke-width="2.5"><path d="M45 4l16 6v13c0 10-7 17-16 20-9-3-16-10-16-20V10z" stroke="var(--green)"/><path d="M38 23l5 5 10-10" stroke="var(--green)"/><circle cx="45" cy="56" r="7"/><path d="M33 80c0-9 5-14 12-14s12 5 12 14z"/><circle cx="24" cy="62" r="6"/><path d="M13 84c0-8 4-12 11-12"/><circle cx="66" cy="62" r="6"/><path d="M77 84c0-8-4-12-11-12"/></svg>
    <h3>Group Insurance</h3>
    <p>Duis aute irure dolor in reprehenderit in voluptate velit esse cillum dolore eu fugiat nulla pariatur</p>
  </div>
  <div class="svc" style="left:437px;top:498px">
    <svg width="90" height="90" viewBox="0 0 90 90" fill="none" stroke="#1e1e1e" stroke-width="2.5"><rect x="22" y="6" width="46" height="78" rx="3"/><path d="M16 10h6v70h-6zM68 10h6v70h-6z"/><rect x="30" y="12" width="30" height="12" stroke="var(--green)"/><text x="45" y="21" font-family="Poppins,sans-serif" font-size="9" font-weight="700" text-anchor="middle" fill="var(--green)" stroke="none">CLAIM</text><path d="M30 34h30M30 42h30M30 50h30M30 58h22"/><circle cx="33" cy="70" r="3"/><path d="M42 72h16"/></svg>
    <h3>Health Claim</h3>
    <p>Duis aute irure dolor in reprehenderit in voluptate velit esse cillum dolore eu fugiat nulla pariatur</p>
  </div>
</section>

<section class="feature" style="left:110px;top:2183px">
  <p class="kicker">INVESTOR</p>
  <h2 class="heading">RELATIONS</h2>
  <p class="body-copy">Lorem Ipsum is simply dummy text of the printing and types etting industry. Lorem Ipsum has been the industry's standa rd dummy text ever since the 1500s, when an unknown printer took a galley of type and scrambled.</p>
  <a class="btn btn-more" href="#">READ MORE</a>
</section>
<div class="photo photo-meeting" role="img" aria-label="Three colleagues discussing a plan around a table with a tablet"></div>

<div class="photo photo-laptop" role="img" aria-label="Man working on a laptop showing financial charts"></div>
<section class="feature" style="left:657px;top:2651px">
  <p class="kicker">INSURANCE</p>
  <h2 class="heading">EDUCATION</h2>
  <p class="body-copy">Lorem Ipsum is simply dummy text of the printing and types etting industry. Lorem Ipsum has been the industry's standa rd dummy text ever since the 1500s, when an unknown printer took a galley of type and scrambled.</p>
  <a class="btn btn-more" href="#">READ MORE</a>
</section>

<section class="testimonials" role="img" aria-label="Green-tinted photo of a happy family playing outdoors">
  <div class="center-head"><p class="kicker">CLIENT</p><h2 class="heading">TESTIMONIALS</h2></div>
  <p class="quote">“ Nemo enim ipsam voluptatem quia voluptas sit aspernatur aut odit aut fugit, sed quia consequuntur magni dolores eos qui ratione voluptatem sequi nesciunt. Neque porro quisquam est, qui dolorem ipsum quia dolor sit amet, consectetur,&nbsp; eius modi tempora incidunt ut labore et dolore magnam aliquamq.”</p>
  <p class="quote-name">- MARCUS REID</p>
  <div class="dots"><span></span><span></span><span></span><span></span></div>
</section>

<section class="appointment">
  <div class="watermark"></div>
  <div class="center-head"><p class="kicker">SET AN</p><h2 class="heading">APPOINTMENT</h2></div>
  <div class="field" style="left:198px;top:211px;width:400px;height:46px">Name</div>
  <div class="field" style="left:198px;top:273px;width:400px;height:48px">Email</div>
  <div class="field" style="left:198px;top:336px;width:400px;height:48px">Phone number</div>
  <div class="field" style="left:610px;top:211px;width:391px;height:173px">Message</div>
  <a class="btn btn-submit" href="#">SUBMIT</a>
</section>

<footer class="footer">
  <div class="footer-brand"><div class="circle"></div><div class="abbr">TFI</div><div class="name">TIDEWATER FAMILY INSURANCE</div></div>
  <div class="links" style="left:385px"><h4>Quick Links</h4><p style="margin-top:8px">Home<br>Services<br>About Us<br>Agents<br>Forms<br>Investor Relations<br>Contact Us</p></div>
  <div class="links" style="left:559px;top:113px"><p>Set an Appointment<br>Testimonials<br>FAQs<br>Careers<br>News and Updates<br>Accessibility Features</p></div>
  <div class="contact">
    <h4 style="margin-bottom:12px">Contact Us</h4>
    <ul>
      <li><svg width="12" height="16" viewBox="0 0 12 16"><path d="M6 0a6 6 0 0 1 6 6c0 4-6 10-6 10S0 10 0 6a6 6 0 0 1 6-6z" fill="var(--green)"/><circle cx="6" cy="6" r="2" fill="var(--dark)"/></svg><span>No 1234 emo enimam volupta tem quia voluptas</span></li>
      <li><svg width="14" height="14" viewBox="0 0 14 14"><path d="M3 0l3 3-2 2c1 2 3 4 5 5l2-2 3 3-2 3C6 14 0 8 0 2z" fill="var(--green)"/></svg><span>1 800 555 0142</span></li>
      <li><svg width="16" height="12" viewBox="0 0 16 12"><rect width="16" height="12" rx="1" fill="var(--green)"/><path d="M1 1l7 6 7-6" stroke="var(--dark)" stroke-width="1.5" fill="none"/></svg><span>info@tfi-insure.com</span></li>
    </ul>
  </div>
  <div class="footer-rule"></div>
  <p class="copyright">© 2024, Tidewater Family Insurance | All Rights Reserved.</p>
  <div class="social"><span><i></i></span><span><i></i></span><span><i></i></span></div>
</footer>

</body>
</html>
```